A business card design for a dental office. We have Two doctors working here. We practice general de

I already have a logo designed for the office with the name and a slogan.
Now I need to create design for a business card using the same logo.
Details Needed on the front side of the card are :
Gerald K. Voskamp, DDS
Marvin R Duchene, DDS
418 Birchwood Lane
Cedar Hollow, ME 06591
Phone : 860 517 4093
Fax : 860 517 4094
Website : WWW.BrightArcDental.Com
Office hours by appointment
On the back side of the card need :
Appointment
Date....................Time...................
With....................................
If unable to keep your appointment, please give 24-48 hours notice in order to avoid broken appointment fee.

Industry/Entity Type

Dental Clinic

Contact Information for Business Card

Gerald K. Voskamp, DDS
Marvin R Duchene, DDS
418 Birchwood Lane
Cedar Hollow, ME 06591
Phone : 860 517 4093
Fax : 860 517 4094
Appointment

Requirements
Must have
• Keep the Name and slogan on the logo on the front of the card. You can move them around the Logo and Name/Slogan of business (Voskamp Family Dentistry/We give you reasons to smile) as you wish to get a feel of the design.
• Gerald K. Voskamp, DDS
• Marvin R Duchene, DDS
• 418 Birchwood Lane
• Cedar Hollow, ME 06591
• Phone : 860 517 4093
• Fax : 860 517 4094
• WWW.BrightArcDental.Com
• Keep these three groups above as they are together now in different areas of the front side.
• On the back side of the card need :
• Appointment
• Date....................Time...................
• With....................................
• If unable to keep your appointment, please give 24-48 hours notice in order to avoid broken appointment fee.

```html
<!DOCTYPE html>
<html lang="en">
<head>
<meta charset="utf-8">
<title>Voskamp Family Dentistry – Business Card</title>
<link rel="stylesheet" href="https://fonts.googleapis.com/css2?family=Montserrat:wght@500;600;700&family=Open+Sans:wght@600;700&display=swap">
<style>
  :root {
    --bg: #e9e9e7;
    --card: #ffffff;
    --teal: #1ba08b;
    --blue: #1b4fa3;
    --red: #d8322f;
    --ink: #1f1f1f;
    --shadow: rgba(0,0,0,0.18);
  }
  * { box-sizing: border-box; margin: 0; padding: 0; }
  html, body { width: 1200px; height: 873px; overflow: hidden; }
  body {
    background: var(--bg);
    font-family: "Montserrat", Arial, sans-serif;
    position: relative;
  }
  .card {
    position: absolute;
    top: 280px;
    width: 550px;
    height: 314px;
    background: var(--card);
    box-shadow: 0 6px 18px var(--shadow);
    overflow: hidden;
  }
  .card--front { left: 30px; }
  .card--back { left: 620px; }

  .brand-name {
    color: var(--blue);
    font-weight: 600;
    font-size: 19px;
    letter-spacing: 0.5px;
    text-transform: uppercase;
    white-space: nowrap;
  }
  .slogan {
    display: flex;
    align-items: center;
    justify-content: center;
    gap: 6px;
    color: var(--red);
    font-size: 6.5px;
    font-weight: 600;
    letter-spacing: 1.2px;
    text-transform: uppercase;
    margin-top: 4px;
    white-space: nowrap;
  }
  .slogan::before, .slogan::after {
    content: "";
    width: 22px;
    height: 1px;
    background: var(--red);
  }

  /* front */
  .front-info {
    position: absolute;
    top: 34px;
    left: 95px;
    width: 360px;
    text-align: center;
  }
  .doctors {
    margin-top: 24px;
    color: var(--blue);
    font-size: 14px;
    font-weight: 600;
    font-variant: small-caps;
    letter-spacing: 1px;
    line-height: 1.3;
  }
  .contact {
    margin-top: 18px;
    color: var(--ink);
    font-size: 12.5px;
    font-weight: 600;
    font-variant: small-caps;
    letter-spacing: 1px;
    line-height: 1.35;
  }
  .website {
    margin-top: 16px;
    color: var(--blue);
    font-size: 11.5px;
    font-weight: 600;
    font-variant: small-caps;
    letter-spacing: 1px;
  }
  .band-rule {
    position: absolute;
    left: 0; right: 0;
    background: var(--blue);
  }
  .band {
    position: absolute;
    left: 0; right: 0; bottom: 0;
    background: var(--teal);
  }
  .card--front .band-rule { top: 232px; height: 6px; }
  .card--front .band {
    top: 238px;
    display: flex;
    align-items: center;
    justify-content: center;
  }
  .address {
    color: var(--ink);
    font-size: 16px;
    font-weight: 600;
    font-variant: small-caps;
    letter-spacing: 1.2px;
    white-space: nowrap;
  }

  /* back */
  .back-brand {
    position: absolute;
    top: 50px;
    left: 110px;
    display: flex;
    align-items: center;
    gap: 16px;
  }
  .brand-dot {
    width: 58px;
    height: 58px;
    border-radius: 50%;
    background: var(--teal);
    flex: none;
  }
  .back-brand .brand-name { font-size: 16px; }
  .back-brand .slogan { justify-content: flex-start; }

  .teal-rule {
    position: absolute;
    left: 0; right: 0;
    top: 168px;
    height: 3px;
    background: var(--teal);
  }
  .appointment-label {
    position: absolute;
    top: 173px;
    left: 0; right: 0;
    text-align: center;
    color: var(--ink);
    font-size: 10px;
    font-weight: 700;
    letter-spacing: 2px;
    text-transform: uppercase;
  }
  .card--back .band-rule { top: 188px; height: 5px; }
  .card--back .band {
    top: 193px;
    padding: 14px 26px;
  }
  .fields {
    display: flex;
    justify-content: space-between;
    color: var(--ink);
    font-size: 11px;
    font-weight: 700;
    letter-spacing: 1.5px;
    text-transform: uppercase;
  }
  .notice {
    margin-top: 16px;
    color: var(--ink);
    font-family: "Open Sans", Arial, sans-serif;
    font-size: 12.5px;
    font-weight: 700;
    line-height: 1.4;
  }
</style>
</head>
<body>

  <section class="card card--front" aria-label="Business card front">
    <div class="front-info">
      <h1 class="brand-name">Voskamp Family Dentistry</h1>
      <p class="slogan">We give you reasons to smile</p>
      <p class="doctors">Gerald K. Voskamp, DDS<br>Marvin R Duchene, DDS</p>
      <p class="contact">Phone : 860 517 4093<br>Fax : 860 517 4094</p>
      <p class="website">Website : www.BrightArcDental.com</p>
    </div>
    <div class="band-rule"></div>
    <div class="band">
      <p class="address">418 Birchwood Lane, Cedar Hollow, ME 06591.</p>
    </div>
  </section>

  <section class="card card--back" aria-label="Business card back">
    <div class="back-brand">
      <span class="brand-dot"></span>
      <div>
        <h2 class="brand-name">Voskamp Family Dentistry</h2>
        <p class="slogan">We give you reasons to smile</p>
      </div>
    </div>
    <div class="teal-rule"></div>
    <p class="appointment-label">Appointment</p>
    <div class="band-rule"></div>
    <div class="band">
      <div class="fields">
        <span>Date ......</span>
        <span>Time ......</span>
        <span>With ......</span>
      </div>
      <p class="notice">If unable to keep your appointment, please give 24-48 hours notice in order to avoid broken appointment fee.</p>
    </div>
  </section>

</body>
</html>
```